BASIC website restyle: graphic + coding

I need a restyle of our present website. Same contents, but better graphic.
It will be temporary until we'll have defined the strategy and so we'll have the definitive one.
I would need a fast job including coding.

I uploaded some picture that you're free to use.
I also extended of 1 day, no more extensions will be possible.

```html
<!DOCTYPE html>
<html lang="en">
<head>
<meta charset="utf-8">
<title>SylvaNet</title>
<link href="https://fonts.googleapis.com/css2?family=Archivo+Black&family=Arimo:wght@400;700&family=Mulish:wght@800&family=Questrial&display=swap" rel="stylesheet">
<style>
  :root{
    --green:#00873f;
    --green-band:rgba(20,140,80,.82);
    --navy:#2e3e50;
    --text:#555b60;
    --white:#ffffff;
    --ink:#2b2420;
  }
  *{box-sizing:border-box;margin:0;padding:0}
  html,body{width:1200px;height:960px;overflow:hidden;background:var(--white)}
  body{font-family:"Arimo",Arial,sans-serif;color:var(--text);position:relative}

  .top-bar{position:absolute;left:0;top:0;width:1200px;height:4px;background:var(--green)}
  .site-header{position:absolute;left:0;top:4px;width:1200px;height:90px}
  .brand{position:absolute;left:150px;top:26px;font-family:"Mulish",sans-serif;font-weight:800;font-size:34px;line-height:36px;color:var(--navy);letter-spacing:.5px}

  .main-nav{position:absolute;left:560px;top:0;height:84px;display:flex}
  .main-nav a{display:block;height:84px;line-height:92px;padding:0 20px;font-size:14px;color:var(--navy);text-decoration:none;position:relative}
  .main-nav a.is-active{background:var(--green);color:var(--white);width:76px;padding:0;text-align:center}
  .main-nav a.is-active::after{content:"";position:absolute;left:33px;bottom:0;border:5px solid transparent;border-bottom-color:var(--white)}

  .hero{position:absolute;left:0;top:94px;width:1200px;height:410px;
    background:radial-gradient(ellipse at 48% 30%,#d9f07a 0%,#9ccc3a 25%,transparent 55%),
               linear-gradient(90deg,#5b7a22 0%,#87b12c 30%,#a4cf3c 55%,#6f9a24 78%,#3f5a1a 100%)}
  .hero-title{position:absolute;left:150px;top:202px}
  .hero-name{display:inline-block;background:var(--navy);color:var(--white);font-family:"Archivo Black",sans-serif;font-size:42px;line-height:48px;padding:0 10px}
  .hero-sub{font-family:"Questrial",sans-serif;font-size:39px;color:var(--white);margin:2px 0 0 9px}

  .intro{position:absolute;left:150px;top:528px;width:554px}
  .intro h1{font-family:"Mulish",sans-serif;font-weight:800;font-size:23px;color:var(--navy);letter-spacing:.5px}
  .intro h1 span{color:var(--green)}
  .intro p{font-size:13.5px;line-height:16px;text-align:justify;margin-top:14px}
  .intro p + p{margin-top:15px}

  .feature{position:absolute;top:702px;width:253px;height:136px;overflow:hidden}
  .feature-forest{left:150px}
  .feature-agri{left:450px}
  .feature-photo{position:absolute;inset:0}
  .feature-forest .feature-photo{background:linear-gradient(160deg,#8a6a4a,#6b4f36 60%,#9a7b5a)}
  .feature-agri .feature-photo{background:linear-gradient(180deg,#b9c9e6 0%,#d8dde4 45%,#7d8a6a 100%)}
  .feature-caption{position:absolute;left:0;bottom:0;width:100%;height:30px;background:var(--green-band);color:var(--white);font-size:17px;line-height:30px;padding-left:9px;font-weight:700}
  .feature-caption .light{font-weight:400}
  .feature-caption svg{position:absolute;right:13px;top:5px}

  .sidebar{position:absolute;left:766px;top:528px;width:285px}
  .side-block{margin-bottom:36px}
  .side-block h2{font-family:"Mulish",sans-serif;font-weight:800;font-size:28px;line-height:26px;color:var(--green)}
  .side-block h3{font-family:"Mulish",sans-serif;font-weight:800;font-size:22px;line-height:22px;color:var(--navy);letter-spacing:.5px;padding-bottom:5px;border-bottom:1px solid var(--navy)}
  .side-block.reference h3{border-bottom-color:var(--green)}
  .partner{display:flex;align-items:center;margin-top:14px}
  .partner-mark{width:62px;height:62px;border-radius:50%;background:#127f86;flex:none}
  .partner-name{font-size:13px;line-height:15px;color:#222;margin-left:10px;margin-top:28px;white-space:nowrap}
  .reference-row{display:flex;align-items:center;margin-top:18px}
  .reference-mark{width:46px;height:46px;border:3px solid var(--ink);flex:none}
  .reference-name{font-family:"Mulish",sans-serif;font-weight:800;font-size:22px;color:var(--ink);letter-spacing:1.5px;margin-left:16px;white-space:nowrap}

  .footer-line{position:absolute;left:0;top:905px;width:1200px;height:5px;background:var(--green)}
  .site-footer{position:absolute;left:0;top:910px;width:1200px;height:50px;background:var(--navy);color:var(--white);font-size:11.5px;text-align:center;line-height:48px}
</style>
</head>
<body>
  <div class="top-bar"></div>
  <header class="site-header">
    <div class="brand">SylvaNet</div>
    <nav class="main-nav">
      <a href="#" class="is-active">Home</a>
      <a href="#">BlazeWatch2</a>
      <a href="#">FieldSense</a>
      <a href="#">Technology</a>
      <a href="#">Contact us</a>
    </nav>
  </header>

  <section class="hero" role="img" aria-label="Sunlit green forest with tree trunks and leaves">
    <div class="hero-title">
      <div class="hero-name">BlazeWatch2</div>
      <div class="hero-sub">Forest Fires Prediction</div>
    </div>
  </section>

  <section class="intro">
    <h1>Welcome to <span>SYLVANET</span></h1>
    <p>Lorem ipsum dolor sit amet, consectetur adipiscing elit. Proin dapibus imperdiet libero at fringilla. Maecenas est nunc, pretium a iaculis sed, blandit ut ligula. Nunc sagittis massa vitae diam imperdiet rutrum.</p>
    <p>Nullam ac fermentum libero, vehicula lobortis lectus. Suspendisse volutpat pulvinar dui a consequat.</p>
  </section>

  <a class="feature feature-forest" href="#">
    <div class="feature-photo" role="img" aria-label="Sensor probe standing in dry autumn leaves"></div>
    <div class="feature-caption">Forest Fires <span class="light">Prediction</span>
      <svg width="20" height="20" viewBox="0 0 20 20"><circle cx="10" cy="10" r="10" fill="#1d3a2c"/><path d="M8 5.5 12.5 10 8 14.5" fill="none" stroke="#fff" stroke-width="2"/></svg>
    </div>
  </a>
  <a class="feature feature-agri" href="#">
    <div class="feature-photo" role="img" aria-label="Weather station among blossoming orchard trees"></div>
    <div class="feature-caption">Agriculture
      <svg width="20" height="20" viewBox="0 0 20 20"><circle cx="10" cy="10" r="10" fill="#1d3a2c"/><path d="M8 5.5 12.5 10 8 14.5" fill="none" stroke="#fff" stroke-width="2"/></svg>
    </div>
  </a>

  <aside class="sidebar">
    <div class="side-block partner-block">
      <h2>SylvaNet</h2>
      <h3>Scientific Partner:</h3>
      <div class="partner">
        <div class="partner-mark"></div>
        <div class="partner-name">Alpine Institute for Forest and<br>Landscape Research</div>
      </div>
    </div>
    <div class="side-block reference">
      <h2>SylvaNet</h2>
      <h3>Scientific Reference:</h3>
      <div class="reference-row">
        <div class="reference-mark"></div>
        <div class="reference-name">ALDER BOARD</div>
      </div>
    </div>
  </aside>

  <div class="footer-line"></div>
  <footer class="site-footer">Copyright © 2013 SylvaNet. All Rights Reserved.</footer>
</body>
</html>
```